Fernquill Stationary Design
The Ledger Desk Firm
Fernquill Stationary Design -
Creative Brief
Professional
Marla Dempton
3847 W. Harlan Pkwy. Suite 410 Irving, TX 75061
mdempton@fernquill.example
www.fernquill.example
We want to be different in our space. Most if not all of our competitors have boring, text-intensive websites. We want to be different. We're agile, nimple, quick, crisp, entrepreneurial, hip/cool.
Logo, Tagline (The Ledger Desk Firm) and our website address (www.fernquill.example) At the end of the day, play around with what looks cool!

```html
<!DOCTYPE html>
<html lang="en">
<head>
<meta charset="utf-8">
<title>Fernquill Business Cards</title>
<link rel="stylesheet" href="https://fonts.googleapis.com/css2?family=Arimo:wght@400;700&display=swap">
<style>
  :root {
    --backdrop: #6e4624;
    --backdrop-light: #7d5330;
    --card: #ffffff;
    --ink: #222222;
    --ink-soft: #333333;
    --wordmark: #4a4a4a;
    --accent: #7cb342;
  }
  * { margin: 0; padding: 0; box-sizing: border-box; }
  html, body { width: 1200px; height: 367px; overflow: hidden; }
  body {
    font-family: "Arimo", Arial, sans-serif;
    color: var(--ink);
  }
  .backdrop {
    position: relative;
    width: 1200px;
    height: 367px;
    background: radial-gradient(ellipse at center, var(--backdrop-light), var(--backdrop));
  }
  .card {
    position: absolute;
    top: 24px;
    width: 562px;
    height: 324px;
    background: var(--card);
    border-radius: 22px;
    box-shadow: 0 2px 6px rgba(0,0,0,0.35);
    overflow: hidden;
  }
  .card--front { left: 19px; }
  .card--back { left: 617px; }

  .holder-name {
    position: absolute;
    top: 30px;
    left: 170px;
    width: 200px;
    text-align: center;
    font-size: 16px;
    font-weight: 700;
  }

  .brand {
    position: absolute;
    display: flex;
    flex-direction: column;
    align-items: center;
  }
  .brand__dot {
    border-radius: 50%;
    background: var(--accent);
  }
  .brand__name {
    font-weight: 700;
    color: var(--wordmark);
    letter-spacing: 1px;
    text-transform: uppercase;
    white-space: nowrap;
  }
  .brand__tagline {
    font-weight: 700;
    color: var(--wordmark);
    text-transform: uppercase;
    white-space: nowrap;
  }

  .card--front .brand { left: 0; top: 118px; width: 230px; }
  .card--front .brand__dot { width: 78px; height: 78px; margin-bottom: 14px; }
  .card--front .brand__name { font-size: 28px; line-height: 1; }
  .card--front .brand__tagline { font-size: 11px; letter-spacing: 1.4px; margin-top: 4px; }

  .contact {
    position: absolute;
    left: 318px;
    top: 104px;
    font-size: 13px;
    line-height: 19px;
    color: var(--ink-soft);
    white-space: nowrap;
  }
  .contact__address { margin-bottom: 18px; }
  .contact__list { list-style: none; }
  .contact__label { display: inline-block; width: 14px; }

  .card--back .brand { left: 0; right: 0; top: 48px; }
  .card--back .brand__dot { width: 100px; height: 100px; margin-bottom: 18px; }
  .card--back .brand__name { font-size: 40px; line-height: 1; }
  .card--back .brand__tagline { font-size: 14px; letter-spacing: 2px; margin-top: 5px; }

  .back-tagline {
    position: absolute;
    left: 0; right: 0;
    top: 238px;
    text-align: center;
    font-size: 14px;
    font-weight: 700;
    text-transform: uppercase;
  }
  .back-web {
    position: absolute;
    left: 0; right: 0;
    top: 270px;
    text-align: center;
    font-size: 14px;
  }
</style>
</head>
<body>
<main class="backdrop">
  <section class="card card--front">
    <p class="holder-name">Marla Dempton</p>
    <div class="brand">
      <span class="brand__dot"></span>
      <span class="brand__name">Fernquill</span>
      <span class="brand__tagline">The Ledger Desk Firm</span>
    </div>
    <div class="contact">
      <p class="contact__address">3847 W. Harlan Pkwy.<br>Suite 410, Irving, TX 75061</p>
      <ul class="contact__list">
        <li><span class="contact__label">P</span>: 972-555-0147</li>
        <li><span class="contact__label">C</span>: 214-555-0182</li>
        <li><span class="contact__label">F</span>: 800-555-0139</li>
        <li><span class="contact__label">E</span>: mdempton@fernquill.example</li>
        <li><span class="contact__label">W</span>: www.fernquill.example</li>
      </ul>
    </div>
  </section>

  <section class="card card--back">
    <div class="brand">
      <span class="brand__dot"></span>
      <span class="brand__name">Fernquill</span>
      <span class="brand__tagline">The Ledger Desk Firm</span>
    </div>
    <p class="back-tagline">The Ledger Desk Firm</p>
    <p class="back-web">www.fernquill.example</p>
  </section>
</main>
</body>
</html>
```